Optometry office needs a postcard to get name out to local schools

I need a postcard design for an optometry office called "Hosaru Optometry".
I want to get our name out to local schools and with this short letter and advertisement.
I want to keep the baby blue /navy blue colors theme.
One the front i want the following
Front:
1) three lines for the address of the recipient as in the example, and square for the postage in the upper right hand corner.
2) our logo with "Hosaru Optometry" and a horizontal line with our website address just below the line as in the example.
put the words "Our practice is committed to supporting our community and local schools." and our phone number "714-390-5264"
3) perhaps more contact info is looks neat and not too cluttered
Back:
1) letter which is attached
2) maybe a small clip art like a phoropter or glasses or something eye related

```html
<!DOCTYPE html>
<html lang="en">
<head>
<meta charset="utf-8">
<title>Hosaru Optometry – School Outreach Postcard</title>
<link href="https://fonts.googleapis.com/css2?family=Lato:ital,wght@0,400;0,700;1,400&family=Fondamento:ital@1&display=swap" rel="stylesheet">
<style>
  :root{
    --baby-blue:#47c3e6;
    --pale-blue:#cdeef8;
    --navy:#2e3192;
    --mist:#e4e5e7;
    --ink:#555a60;
    --rule:#8c8f94;
    --paper:#ffffff;
    --backdrop:#eceae6;
  }
  *{margin:0;padding:0;box-sizing:border-box}
  html,body{width:957px;height:1200px;overflow:hidden}
  body{background:var(--backdrop);font-family:"Lato",sans-serif;position:relative}

  .postcard{position:absolute;width:750px;height:534px;background:var(--paper);overflow:hidden;
    box-shadow:0 4px 10px rgba(0,0,0,.18)}
  .postcard--letter{left:51px;top:45px}
  .postcard--mailer{left:142px;top:615px}

  .card-art{position:absolute;inset:0}

  .brand{position:absolute;display:flex;align-items:center;gap:10px;color:var(--navy);
    font-family:"Lato",sans-serif;font-weight:400;white-space:nowrap}
  .brand__dot{width:16px;height:16px;border-radius:50%;background:var(--baby-blue)}
  .postcard--letter .brand{left:30px;top:52px;font-size:32px}

  .letter__greeting{position:absolute;left:33px;top:278px;font-size:16px;color:#222}
  .letter__body{position:absolute;left:22px;top:331px;width:700px;color:var(--paper);
    font-size:11.6px;line-height:14.2px}
  .letter__body p{margin-bottom:1px}
  .letter__sign{position:absolute;right:40px;top:491px;color:var(--paper);font-style:italic;font-size:15px;word-spacing:6px}

  .postcard--mailer .brand{left:34px;top:58px;font-size:34px}
  .mailer__doctor{position:absolute;left:245px;top:104px;color:var(--navy);font-style:italic;font-size:16px}
  .mailer__rule{position:absolute;left:32px;top:141px;width:320px;height:2px;background:var(--navy)}
  .mailer__web{position:absolute;left:75px;top:149px;font-size:16px;color:var(--ink);letter-spacing:.3px}
  .mailer__pledge{position:absolute;left:40px;top:201px;width:330px;font-family:"Fondamento",serif;
    font-style:italic;font-size:19px;line-height:25px;color:var(--ink)}
  .mailer__contact{position:absolute;left:33px;top:302px;color:var(--ink);font-size:13px}
  .contact__lead{margin-bottom:6px}
  .contact__row{display:flex;align-items:center;gap:6px;font-size:15px}
  .contact__row .email{font-size:12px;margin-left:26px}
  .contact__row svg{width:16px;height:16px;flex:none}
  .contact__address{margin-top:8px;margin-left:10px;font-size:13px}

  .mailer__stamp{position:absolute;left:636px;top:34px;width:80px;height:80px;border:2px solid #9a9da1}
  .mailer__address-lines{position:absolute;left:443px;top:189px;width:271px}
  .mailer__address-lines span{display:block;height:32px;border-bottom:1.5px solid #a3a6aa}
  .mailer__address-lines span:first-child{height:0}
</style>
</head>
<body>

<section class="postcard postcard--letter" aria-label="Letter side of postcard">
  <svg class="card-art" viewBox="0 0 750 534" width="750" height="534" aria-hidden="false">
    <defs>
      <linearGradient id="portraitTone" x1="0" y1="0" x2="1" y2="0">
        <stop offset="0" stop-color="#e9edf1"/>
        <stop offset=".4" stop-color="#e8cdbd"/>
        <stop offset=".75" stop-color="#f3f3f4"/>
        <stop offset="1" stop-color="#d9dcdf"/>
      </linearGradient>
    </defs>
    <rect role="img" aria-label="Photo of a smiling woman adjusting black eyeglasses in front of a blurred eye chart" x="0" y="0" width="750" height="300" fill="url(#portraitTone)"/>
    <path d="M0 256 C250 240 500 252 750 200 L750 534 L0 534 Z" fill="var(--mist)"/>
    <path d="M0 308 C260 300 560 262 750 100 L750 534 L0 534 Z" fill="var(--baby-blue)"/>
    <circle cx="614" cy="222" r="92" fill="var(--pale-blue)"/>
    <circle role="img" aria-label="Photo of a phoropter eye examination instrument" cx="614" cy="222" r="84" fill="#d6d8db"/>
  </svg>

  <div class="brand"><span class="brand__dot"></span>Hosaru Optometry</div>

  <p class="letter__greeting">Dear</p>
  <div class="letter__body">
    <p>I would like to introduce our family optometry office that has been in business for the past 35 years! We are located at 4120 Orchard Grove Ave Ste B in Fairview (near Orchard Grove Ave and Maple Blvd).</p>
    <p>Our practice is committed to supporting our community and local schools by taking care of adults and children of all ages. As 80% of learning is done visually, it is especially important for young children to have access to routine comprehensive eye care. Our goal is to provide excellent eye care for families as well as quality ophthalmic frames and lenses at reasonable prices.</p>
    <p>We are happy to see any referrals from you, including students who have not passed vision screenings or have other ocular health concerns. Please feel free to reach out to us if you have any questions. You can contact us by phone or email, and are also welcome to visit our office anytime.</p>
    <p>We look forward to a strong relationship together and success for all your students.</p>
  </div>
  <p class="letter__sign">Sincerely, Kenji Hosaru, OD</p>
</section>

<section class="postcard postcard--mailer" aria-label="Address side of postcard">
  <svg class="card-art" viewBox="0 0 750 534" width="750" height="534" aria-hidden="true">
    <path d="M0 470 C250 462 560 452 750 420 L750 534 L0 534 Z" fill="var(--mist)"/>
    <path d="M0 482 C260 478 560 466 750 436 L750 534 L0 534 Z" fill="var(--baby-blue)"/>
  </svg>

  <div class="brand"><span class="brand__dot"></span>Hosaru Optometry</div>
  <p class="mailer__doctor">Kenji Hosaru, OD</p>
  <div class="mailer__rule"></div>
  <p class="mailer__web">www.hosaruoptometry.com</p>

  <p class="mailer__pledge">Our practice is committed to supporting our community and local schools.</p>

  <div class="mailer__contact">
    <p class="contact__lead">Contact us today for a free, no obligation consultation:</p>
    <div class="contact__row">
      <svg viewBox="0 0 16 16" aria-hidden="true"><circle cx="8" cy="8" r="7" fill="none" stroke="#555a60" stroke-width="1.4"/><path d="M5.3 4.2 L6.6 5.8 L5.9 6.9 C6.5 8.2 7.6 9.3 9 9.9 L10.1 9.3 L11.7 10.6 L10.8 11.9 C7.5 11.4 4.6 8.5 4.1 5.2 Z" fill="#555a60"/></svg>
      <span>714-390-5264</span>
      <svg viewBox="0 0 16 16" aria-hidden="true" style="margin-left:28px"><rect x="2" y="5" width="12" height="8" fill="#555a60"/><path d="M2 6 L8 2 L14 6" fill="none" stroke="#555a60" stroke-width="1.4"/><path d="M3 6 L8 9.5 L13 6" fill="none" stroke="#fff" stroke-width="1.2"/></svg>
      <span class="email" style="margin-left:0">hello@hosaruoptometry.com</span>
    </div>
    <p class="contact__address">4120 Orchard Grove Ave Ste B Fairview, CA 90418</p>
  </div>

  <div class="mailer__stamp" aria-label="Postage stamp area"></div>
  <div class="mailer__address-lines" aria-label="Recipient address lines">
    <span></span><span></span><span></span><span></span>
  </div>
</section>

</body>
</html>
```